Elegant, Playful ReDesign of Paperlark Website in wordpress - Budget has been raised

Project Brief: Paperlark Website Redesign in WordPress

Introduction: Paperlark, a cutting-edge document creation solution, aims to revolutionize the tedious process of crafting contracts, offers, forms, and other documents. By saving customers valuable time, streamlining workflows, and minimizing human error, Paperlark has become an essential tool. As a technology company with a diverse clientele, we're set to boost our online presence through a refreshed WordPress website. Beyond a modernized website, we aspire to establish a stronger brand identity, incorporating graphic elements seamlessly into our online presence.

Current Status: Currently hosted on WordPress, Paperlark's existing website serves its purpose but is ready for a visual transformation. Our goal is to maintain a modern and attractive appearance while upholding our commitment to simplicity and efficiency. Notably, the website is currently only in Danish. The redesigned structure should include a language switch function to cater to future international customers.

Objectives:
• Modern Aesthetic: Redesign the website with a fresh and modern vibe, reflecting innovation in the document creation sphere.
• User-Friendly: Prioritize an intuitive design for seamless navigation, ensuring visitors easily understand our offerings and benefits.
• Informative Content: Strike a balance between attractiveness and informativeness, clearly communicating Paperlark's value proposition and simplifying business processes.
• Graphic Elements: Integrate visually appealing graphics that enhance the site's aesthetics and contribute to our overall visual identity. These elements should be versatile for future use in social media, advertisements, and other branding materials.
• Brand Recognition: Maintain our current logo and color scheme while exploring creative ways to establish a distinctive brand identity. The website should be a cornerstone for a cohesive branding strategy.
• Media Integration: Include images or videos on the website to enhance engagement. Find suitable, free-to-use visuals.
• Responsiveness: Ensure the design is responsive and works seamlessly on all devices.
• Demo Booking Form: Improve the design of the form to book a demo.
• Multilingual Support: Enable language transformation; the website is currently in Danish but should cater to other countries.

Guidelines:
• Typography: Up to the designer's discretion.
• Images/Videos: Must be free to use without additional charges.
• WordPress Theme: Use any WordPress theme below $100.
• Logo Redesign: Not needed; stick to the referenced color palette, as our new logo uses these colors.
• Color Palette: Stick to the existing company colors for consistency:
RGB
• #000b3c
• #004c6c
• #319ac3
• Greytones and white are also allowed
• Creativity Encouraged: Embrace creativity within the color palette for the layout, visuals, and overall user experience.

Conclusion: The Paperlark website redesign marks an exciting opportunity to enhance our online presence. Our goal is to achieve a balance between a modern, attractive design and a clear, informative representation of our innovative solutions. We envision the revamped website as the foundation for a compelling online brand presence, with versatile graphic elements resonating across various digital platforms.

Sections that the website must include: Space for customer logos, space for testimonials, Space and redesign for display of price structure and price comparison, sections for company details and other information.

Design should also include a redesign of the customer cases section.
Generally there should just be a redesign of all things that are on the website.

Link to current website: https://paperlark-example.com/

+50 employees.

Document automation

Coded - Design and coding required

5+ page

0054AA
0677BA
7BADD7
CADEEF
E8F1F8

• The new webpage must have the same pages as the current one. Frontpage, Book demo, About us, Case stories and Pricing

```html
<!DOCTYPE html>
<html lang="da">
<head>
<meta charset="utf-8">
<title>Paperlark – Om os</title>
<link href="https://fonts.googleapis.com/css2?family=Montserrat:wght@600;700;800&family=Poppins:wght@400;500;600&display=swap" rel="stylesheet">
<style>
:root{
  --navy:#000b3c;
  --teal:#004c6c;
  --blue:#319ac3;
  --bright:#0677ba;
  --soft:#cadeef;
  --mist:#e8f1f8;
  --grey:#f4f6f8;
  --text:#5b6270;
  --white:#fff;
}
*{margin:0;padding:0;box-sizing:border-box}
html,body{width:1200px;height:3664px;overflow:hidden}
body{font-family:"Poppins",sans-serif;color:var(--text);background:var(--white);position:relative}
.abs{position:absolute}
h1,h2,h3,h4{font-family:"Montserrat",sans-serif;color:var(--teal)}

/* header */
.site-header{top:0;left:0;width:1200px;height:64px;padding:0 80px;display:flex;align-items:center;justify-content:space-between;box-shadow:0 2px 10px rgba(0,0,0,.05)}
.brand{display:flex;align-items:center;gap:10px;font-family:"Poppins",sans-serif;font-weight:600;font-size:22px;color:var(--teal);letter-spacing:1px}
.brand-mark{width:22px;height:22px;background:var(--blue);border-radius:4px}
.nav{display:flex;gap:34px;align-items:center;font-size:15px;font-weight:500;color:var(--navy)}
.nav .active{color:var(--blue)}
.btn{background:var(--blue);color:#fff;font-size:13px;font-weight:600;padding:10px 22px;border-radius:4px;letter-spacing:.5px}

/* intro */
.page-title{top:160px;width:1200px;text-align:center;font-size:58px;font-weight:800}
.features{top:400px;left:80px;width:470px}
.feature{display:flex;gap:22px;margin-bottom:58px}
.feature-icon{flex:none;width:56px;height:56px;border-radius:50%;background:var(--teal);display:flex;align-items:center;justify-content:center}
.feature h3{font-size:17px;font-weight:700;margin-bottom:6px}
.feature p{font-size:12px;line-height:1.6}
.hero-art{top:330px;left:610px;width:520px;height:470px;border-radius:48% 52% 40% 60%/55% 45% 55% 45%;background:radial-gradient(circle at 45% 45%,#e8f1f8 0 34%,#7badd7 35% 60%,#319ac3 61%)}

/* history */
.section-title{width:1200px;text-align:center;font-size:42px;font-weight:800}
.history-text{top:910px;left:100px;width:1000px;font-size:12.5px;line-height:1.9;text-align:center}
.history-text p{margin-bottom:26px}
.history-text strong{color:var(--navy)}

/* timeline */
.timeline-bg{top:1360px;left:0;width:1200px;height:1120px;background:var(--grey)}
.timeline-line{top:1440px;left:128px;width:2px;height:950px;background:var(--blue)}
.dot{left:122px;width:14px;height:14px;border-radius:50%;background:var(--white);border:3px solid var(--blue)}
.year{left:168px;font-size:13px;font-weight:600;color:var(--navy)}
.tl-card{left:160px;width:960px;background:var(--white);border-radius:6px;box-shadow:0 6px 24px rgba(0,11,60,.08);padding:0 40px;display:flex;flex-direction:column;justify-content:center}
.tl-card h4{font-size:22px;font-weight:600;color:var(--navy);margin-bottom:10px}
.tl-card p{font-size:12.5px;line-height:1.7}
.tl-icon{position:absolute;right:28px;top:22px}

/* leadership */
.leader{top:2760px;width:320px;height:460px;background:var(--white);border-radius:6px;box-shadow:0 8px 28px rgba(0,11,60,.1);text-align:center;padding:30px 26px}
.portrait{width:150px;height:150px;border-radius:50%;margin:0 auto 22px;background:linear-gradient(160deg,#cadeef,#7badd7 60%,#004c6c)}
.leader h4{font-size:22px;font-weight:700;color:var(--bright)}
.leader .role{font-size:11px;margin:4px 0 16px;color:#8a909c}
.leader p{font-size:11px;line-height:1.7}
.socials{display:flex;gap:10px;justify-content:center;margin-top:20px}
.socials span{width:28px;height:28px;border-radius:50%;background:var(--bright)}

/* footer */
.footer{top:3300px;left:0;width:1200px;height:340px;background:var(--navy);color:#fff;padding:60px 80px;display:flex}
.footer-col{width:346px}
.footer .brand{color:#fff;font-size:20px}
.footer .tagline{font-size:17px;line-height:1.5;margin:22px 0 18px;font-weight:500}
.footer .socials{justify-content:flex-start}
.footer .socials span{background:var(--blue)}
.footer h5{font-family:"Montserrat",sans-serif;font-size:15px;color:var(--blue);margin-bottom:18px;font-weight:700}
.footer li{list-style:none;font-size:13px;margin-bottom:12px;display:flex;gap:10px;align-items:center}
.copyright{top:3640px;left:0;width:1200px;height:24px;background:var(--blue);color:#fff;font-size:11px;text-align:center;line-height:24px}
</style>
</head>
<body>

<header class="site-header abs">
  <div class="brand"><span class="brand-mark"></span>PAPERLARK</div>
  <nav class="nav">
    <span>Forside</span><span>Kundecases</span><span class="active">Video</span><span>Live Demo</span><span>Priser</span><span>Om os</span>
    <span class="btn">BOOK DEMO</span>
  </nav>
</header>

<h1 class="page-title abs">Om Os</h1>

<div class="features abs">
  <div class="feature">
    <div class="feature-icon"><svg width="26" height="26" viewBox="0 0 26 26" fill="none" stroke="#fff" stroke-width="2"><rect x="3" y="5" width="20" height="13" rx="2"/><path d="M9 22h8M13 18v4"/></svg></div>
    <div><h3>AVANCERET SOFTWARE</h3><p>Vi har på få sekunder softwaren der samler oplysninger og laver færdige dokumenter til dig.</p></div>
  </div>
  <div class="feature">
    <div class="feature-icon"><svg width="26" height="26" viewBox="0 0 26 26" fill="none" stroke="#fff" stroke-width="2"><circle cx="13" cy="13" r="9"/><path d="M13 8v5l3 3"/></svg></div>
    <div><h3>TILGÆNGELIGHED</h3><p>Vi er altid klar til at hjælpe, og vores løsning kan tilgås hvor som helst og når det passer dig.</p></div>
  </div>
  <div class="feature">
    <div class="feature-icon"><svg width="26" height="26" viewBox="0 0 26 26" fill="none" stroke="#fff" stroke-width="2"><path d="M5 21C5 10 12 5 22 5c0 10-5 16-15 16z"/><path d="M5 21l9-9"/></svg></div>
    <div><h3>GRØNT AFTRYK</h3><p>Vi arbejder papirløst og digitalt, så vi sparer både tid, ressourcer og miljø for alle kunder.</p></div>
  </div>
</div>

<div class="hero-art abs" role="img" aria-label="Illustration: person holding a pen beside a large signed consent document"></div>

<h2 class="section-title abs" style="top:820px">HISTORIE</h2>
<div class="history-text abs">
  <p>Paperlark blev grundlagt med et ønske om at gøre det let og hurtigt at skabe juridiske dokumenter. Vi så et behov i markedet for en enkel, digital løsning, og idéen blev til hos stifteren <strong>Mikkel Varming</strong>, der ville spare tid for kunder og partnere.</p>
  <p>Siden har vi udviklet en intelligent dokumentløsning, der samler data fra formularer og skaber kontrakter, tilbud og aftaler helt automatisk. Løsningen kan tilpasses enhver virksomhed og bruges som white label.</p>
  <p>De første advokatfirmaer tog løsningen i brug kort efter, og samarbejdet med Nordvig Dokument gav os en stærk partner. I dag hjælper vi over halvtreds virksomheder med at spare tid og undgå fejl i deres papirarbejde.</p>
  <p>Vi fortsætter med at udvikle nye funktioner og investere i teknologi, der gør dokumenthåndtering enkel for alle.</p>
</div>

<div class="timeline-bg abs"></div>
<div class="timeline-line abs"></div>

<span class="year abs" style="top:1422px">2017</span>
<span class="dot abs" style="top:1520px"></span>
<div class="tl-card abs" style="top:1488px;height:96px">
  <svg class="tl-icon" width="24" height="24" viewBox="0 0 24 24" fill="none" stroke="#319ac3" stroke-width="1.8"><path d="M4 10a11 11 0 0 1 16 0M7 13a7 7 0 0 1 10 0M10 16a3 3 0 0 1 4 0"/></svg>
  <h4>Idé</h4>
  <p>Efter at have oplevet hvor besværligt og dyrt det var at oprette juridiske dokumenter, så vi en mulighed i at gøre hele processen digital.</p>
</div>

<span class="year abs" style="top:1722px">2018</span>
<span class="dot abs" style="top:1850px"></span>
<div class="tl-card abs" style="top:1780px;height:160px">
  <svg class="tl-icon" width="24" height="24" viewBox="0 0 24 24" fill="none" stroke="#319ac3" stroke-width="1.8"><path d="M4 9h4l6-4v14l-6-4H4z"/></svg>
  <h4>Første advokat løsninger</h4>
  <p>Vi udviklede den intelligente dokumentløsning til et advokatfirma, og det resulterede hurtigt i, at flere så fordelene ved et white label setup.</p>
</div>

<span class="year abs" style="top:2006px">2020</span>
<span class="dot abs" style="top:2134px"></span>
<div class="tl-card abs" style="top:2060px;height:160px">
  <svg class="tl-icon" width="24" height="24" viewBox="0 0 24 24" fill="none" stroke="#319ac3" stroke-width="1.8"><rect x="5" y="3" width="14" height="18" rx="2"/><path d="M9 8h6M9 12h6M9 16h4"/></svg>
  <h4>Strategisk samarbejde</h4>
  <p>Ved at indgå et strategisk samarbejde med Nordvig Dokument kunne vi tilbyde vores løsning til endnu flere advokatkontorer. Nu kan alle advokatvirksomheder skabe juridiske dokumenter med deres eget brand, uden at skulle have deres eget system.</p>
</div>

<span class="year abs" style="top:2326px">2021</span>
<span class="dot abs" style="top:2400px"></span>
<div class="tl-card abs" style="top:2360px;height:100px">
  <svg class="tl-icon" width="24" height="24" viewBox="0 0 24 24" fill="none" stroke="#319ac3" stroke-width="1.8"><path d="M3 17l6-6 4 4 8-8M15 7h6v6"/></svg>
  <h4>Ny investor</h4>
  <p>Nogle år senere fik vi en investor om bord, som hjalp os med at sætte skub i væksten og udvikle endnu flere funktioner til vores kunder.</p>
</div>

<h2 class="section-title abs" style="top:2640px">LEDELSE</h2>

<div class="leader abs" style="left:80px">
  <div class="portrait" role="img" aria-label="Portrait photo of the founder"></div>
  <h4>Mikkel Varming</h4>
  <div class="role">CEO · Medstifter</div>
  <p>Mikkel har i mange år arbejdet med digitale løsninger og drevet flere virksomheder. Han står bag idéen og leder udviklingen af produktet i dag.</p>
  <div class="socials"><span></span><span></span></div>
</div>
<div class="leader abs" style="left:440px">
  <div class="portrait" role="img" aria-label="Portrait photo of the CTO"></div>
  <h4>Jesper Holmgaard</h4>
  <div class="role">CTO · Medstifter</div>
  <p>Jesper har en baggrund i softwareudvikling og ansvarer for den tekniske platform. Han sikrer, at løsningen er stabil, sikker og nem at bruge.</p>
  <div class="socials"><span></span><span></span></div>
</div>
<div class="leader abs" style="left:800px">
  <div class="portrait" role="img" aria-label="Portrait photo of the sales director"></div>
  <h4>Rasmus Lindquist Brandt</h4>
  <div class="role">Salgsdirektør</div>
  <p>Rasmus har mange års erfaring med salg til advokatbranchen og hjælper nye kunder godt i gang med løsningen og deres egne skabeloner.</p>
  <div class="socials"><span></span><span></span></div>
</div>

<footer class="footer abs">
  <div class="footer-col">
    <div class="brand"><span class="brand-mark"></span>PAPERLARK</div>
    <p class="tagline">Opnå hjælp til kontrakter og tilbud hurtigt</p>
    <div class="socials"><span></span><span></span><span></span></div>
  </div>
  <div class="footer-col">
    <h5>Features</h5>
    <ul>
      <li><svg width="14" height="14" viewBox="0 0 14 14" fill="none" stroke="#319ac3" stroke-width="2"><path d="M2 7l3 3 7-7"/></svg>Få altid tilbud automatisk</li>
      <li><svg width="14" height="14" viewBox="0 0 14 14" fill="none" stroke="#319ac3" stroke-width="2"><path d="M2 7l3 3 7-7"/></svg>Få jeres kontrakter automatisk</li>
      <li><svg width="14" height="14" viewBox="0 0 14 14" fill="none" stroke="#319ac3" stroke-width="2"><path d="M2 7l3 3 7-7"/></svg>Gem manuelt arbejde</li>
      <li><svg width="14" height="14" viewBox="0 0 14 14" fill="none" stroke="#319ac3" stroke-width="2"><path d="M2 7l3 3 7-7"/></svg>Underskriv digitalt</li>
    </ul>
  </div>
  <div class="footer-col">
    <h5>KONTAKT</h5>
    <ul>
      <li><svg width="14" height="14" viewBox="0 0 14 14" fill="none" stroke="#319ac3" stroke-width="1.6"><rect x="1" y="3" width="12" height="8"/><path d="M1 3l6 5 6-5"/></svg>kontakt@paperlark-example.com</li>
      <li><svg width="14" height="14" viewBox="0 0 14 14" fill="none" stroke="#319ac3" stroke-width="1.6"><path d="M3 1h3l1 3-2 1a7 7 0 0 0 4 4l1-2 3 1v3a1 1 0 0 1-1 1A11 11 0 0 1 2 2a1 1 0 0 1 1-1z"/></svg>+45 20 00 11 22</li>
      <li><svg width="14" height="14" viewBox="0 0 14 14" fill="none" stroke="#319ac3" stroke-width="1.6"><path d="M7 13s5-5 5-8A5 5 0 0 0 2 5c0 3 5 8 5 8z"/><circle cx="7" cy="5" r="1.5"/></svg>Lærkevej 14, 2750 Eksempelby</li>
    </ul>
  </div>
</footer>
<div class="copyright abs">Copyright © 2023 · All Rights Reserved</div>

</body>
</html>
```